Bref créative
Brightfield pest control
Stationary business card project for brightfield pest control
Professional
Doug Harlan
4120 w pinecrest ln. meridian idaho 83619
dharlan77@mailvista.net
ALL SERVICES GUARANTEED
Residential.Commercial Service.Certified specialist.Free Estimates
This is the company logo.

```html
<!DOCTYPE html>
<html lang="en">
<head>
<meta charset="utf-8">
<title>Brightfield pest control – stationery</title>
<link href="https://fonts.googleapis.com/css2?family=Roboto+Condensed:wght@400;700&display=swap" rel="stylesheet">
<style>
:root{
  --green:#2ba84a;
  --green-faint:#e3f1e6;
  --orange:#f7941d;
  --ink:#333333;
  --paper:#ffffff;
  --backdrop:#e9e9e9;
  --shadow:0 2px 6px rgba(0,0,0,.25);
}
*{margin:0;padding:0;box-sizing:border-box}
html,body{width:1200px;height:854px;overflow:hidden}
body{background:var(--backdrop);position:relative;font-family:"Roboto Condensed",Arial,sans-serif;color:var(--ink)}
.sheet{position:absolute;background:var(--paper);box-shadow:var(--shadow);overflow:hidden}
.sheet svg.shape{position:absolute;inset:0;width:100%;height:100%}

.brand{display:flex;align-items:center;gap:6px;color:var(--green);font-weight:700;line-height:1;position:absolute}
.brand .dot{border-radius:50%;background:var(--green);flex:none}

.services{position:absolute;font-size:8px;line-height:1.25;font-weight:700}
.services .headline{color:var(--green)}
.fine{position:absolute;font-size:6px;line-height:1.45}

/* letterhead */
.letterhead{left:43px;top:29px;width:514px;height:739px}
.letterhead .brand{left:18px;top:26px;font-size:17px}
.letterhead .brand .dot{width:22px;height:22px}
.letterhead .services{left:360px;top:14px}
.letterhead .fine{left:14px;top:681px}
.letterhead .watermark{position:absolute;left:220px;top:450px;width:240px;height:240px;border-radius:50%;background:var(--green-faint);display:flex;align-items:center;justify-content:center;color:#d2e8d7;font-weight:700;font-size:22px;text-align:center}

/* business card front */
.card-front{left:605px;top:29px;width:216px;height:144px;border-radius:8px}
.card-front .brand{left:12px;top:14px;font-size:10px}
.card-front .brand .dot{width:12px;height:12px}
.card-front .services{left:12px;top:54px;font-size:5.5px}
.card-front .contact{position:absolute;right:10px;top:44px;color:#fff;text-align:right;font-size:5px;line-height:1.5}
.card-front .contact .name{font-size:9px;font-weight:700}

/* business card back */
.card-back{left:833px;top:29px;width:156px;height:144px;border-radius:8px}
.card-back .brand{left:22px;top:40px;font-size:11px;flex-direction:column;gap:5px;text-align:center;width:112px}
.card-back .brand .dot{width:16px;height:16px}

/* compliment slip */
.slip{left:605px;top:192px;width:547px;height:288px}
.slip .brand{left:22px;top:24px;font-size:15px}
.slip .brand .dot{width:20px;height:20px}
.slip .services{left:22px;top:70px;font-size:7px}
.slip .fine{left:22px;top:242px}
.slip .mark{position:absolute;left:410px;top:88px;width:96px;height:96px;border-radius:50%;background:rgba(255,255,255,.22)}

/* envelope */
.envelope{left:600px;top:509px;width:552px;height:283px}
.envelope .brand{left:0;right:0;top:116px;justify-content:center;font-size:22px}
.envelope .brand .dot{width:26px;height:26px}
</style>
</head>
<body>

<section class="sheet letterhead" aria-label="Letterhead">
  <svg class="shape" viewBox="0 0 514 739" preserveAspectRatio="none">
    <path d="M452 0 C470 14 488 26 514 32 L514 0Z" fill="var(--orange)"/>
    <path d="M462 0 C478 10 494 18 514 22 L514 0Z" fill="var(--green)"/>
    <rect x="0" y="727" width="514" height="12" fill="var(--green)"/>
    <path d="M430 739 C450 733 470 727 514 724 L514 739Z" fill="var(--orange)"/>
  </svg>
  <div class="brand"><span class="dot"></span>brightfield pest control</div>
  <div class="services">
    <div class="headline">ALL SERVICES GUARANTEED</div>
    <div>Residential</div><div>Commercial Service</div><div>Certified specialist</div><div>Free Estimates</div>
  </div>
  <div class="watermark">brightfield<br>pest control</div>
  <div class="fine">Address: 4120 w pinecrest ln. meridian idaho 83619<br>Tel: (208) 555-0147<br>E-mail: dharlan77@mailvista.net</div>
</section>

<section class="sheet card-front" aria-label="Business card front">
  <svg class="shape" viewBox="0 0 216 144" preserveAspectRatio="none">
    <path d="M70 144 C95 80 130 30 170 0 L216 0 L216 144Z" fill="var(--orange)"/>
    <path d="M84 144 C108 84 142 36 186 0 L216 0 L216 144Z" fill="var(--green)"/>
  </svg>
  <div class="brand"><span class="dot"></span>brightfield pest control</div>
  <div class="services">
    <div class="headline">ALL SERVICES GUARANTEED</div>
    <div>Residential</div><div>Commercial Service</div><div>Certified specialist</div><div>Free Estimates</div>
  </div>
  <div class="contact">
    <div class="name">Doug Harlan</div>
    <div>4120 w pinecrest ln.</div>
    <div>meridian idaho 83619</div>
    <div>Tel: (208) 555-0147</div>
    <div>dharlan77@mailvista.net</div>
  </div>
</section>

<section class="sheet card-back" aria-label="Business card back">
  <svg class="shape" viewBox="0 0 156 144" preserveAspectRatio="none">
    <path d="M60 144 C95 130 130 110 156 80 L156 144Z" fill="var(--orange)"/>
    <path d="M74 144 C106 132 136 114 156 92 L156 144Z" fill="var(--green)"/>
  </svg>
  <div class="brand"><span class="dot"></span>brightfield pest control</div>
</section>

<section class="sheet slip" aria-label="Compliment slip">
  <svg class="shape" viewBox="0 0 547 288" preserveAspectRatio="none">
    <path d="M290 288 C340 200 380 80 500 0 L547 0 L547 288Z" fill="var(--orange)"/>
    <path d="M312 288 C360 200 400 90 530 0 L547 0 L547 288Z" fill="var(--green)"/>
  </svg>
  <div class="mark"></div>
  <div class="brand"><span class="dot"></span>brightfield pest control</div>
  <div class="services">
    <div class="headline">ALL SERVICES GUARANTEED</div>
    <div>Residential</div><div>Commercial Service</div><div>Certified specialist</div><div>Free Estimates</div>
  </div>
  <div class="fine">Address: 4120 w pinecrest ln.<br>meridian idaho 83619<br>Tel: (208) 555-0147<br>E-mail: dharlan77@mailvista.net</div>
</section>

<section class="sheet envelope" aria-label="Envelope">
  <svg class="shape" viewBox="0 0 552 283" preserveAspectRatio="none">
    <rect x="0" y="0" width="552" height="68" fill="var(--green)"/>
    <path d="M0 0 L552 0 L520 38 L32 38Z" fill="#259a43"/>
  </svg>
  <div class="brand"><span class="dot"></span>brightfield pest control</div>
</section>

</body>
</html>
```